Small Business Broker Business Card Design

A business card design for a small business brokerage, which is a financial service, not unlike real estate brokerage, but for small businesses such as laundromats, pizza shops, restaurants, cleaners etc. The designs should all be simple, more conservative in nature, using the colors and font of the logo. Again, think real estate Brokerage as a business context
Contact Information for Business Card
Name: Dale R. Whitmore. Title: Small Business Advisor. Email: d.whitmore@lanternbridgeadvisory.com. Mobile: (917) 555-0148. Office: (718) 555-0193. www.lanternbridgeadvisory.com

```html
<!DOCTYPE html>
<html lang="en">
<head>
<meta charset="utf-8">
<title>Lantern Bridge Advisory – Business Card</title>
<link href="https://fonts.googleapis.com/css2?family=Roboto+Condensed:wght@400;700&display=swap" rel="stylesheet">
<style>
  :root {
    --green: #6ea22f;
    --navy: #1f3b60;
    --ink: #1d1d1d;
    --card: #f3efe7;
    --page: #e4dfd6;
    --rule: #3a3a3a;
    --band-text: #eef5e2;
  }
  * { margin: 0; padding: 0; box-sizing: border-box; }
  html, body { width: 1200px; height: 1046px; overflow: hidden; background: var(--page); }
  body { position: relative; font-family: "Roboto Condensed", Arial, sans-serif; color: var(--ink); }

  .card {
    position: absolute; left: 100px; top: 250px;
    width: 1000px; height: 546px;
    background: var(--card);
    border-radius: 28px;
    overflow: hidden;
    box-shadow: 0 6px 24px rgba(0,0,0,.12);
  }

  /* Brand block */
  .brand { position: absolute; left: 40px; top: 180px; width: 376px; text-align: center; }
  .brand-square { width: 58px; height: 58px; background: var(--navy); margin: 0 auto 30px; }
  .brand-name {
    font-weight: 700; font-size: 21px; letter-spacing: 1.2px;
    color: var(--navy); text-transform: uppercase; white-space: nowrap;
  }
  .brand-tagline {
    margin-top: 3px; font-size: 10.5px; font-weight: 700; letter-spacing: 1.4px;
    color: var(--green); text-transform: uppercase; white-space: nowrap;
  }

  .divider { position: absolute; left: 501px; top: 102px; width: 1.5px; height: 330px; background: var(--rule); }

  /* Contact block */
  .person { position: absolute; left: 565px; top: 170px; }
  .person-name { font-weight: 700; font-size: 44px; line-height: 1; color: var(--green); letter-spacing: -.5px; }
  .person-title { font-size: 22px; margin-top: 6px; }

  .contacts { position: absolute; left: 574px; top: 283px; list-style: none; }
  .contacts li { display: flex; align-items: center; height: 30px; font-size: 22px; white-space: nowrap; }
  .contacts svg { width: 18px; height: 18px; margin-right: 13px; flex: none; }

  /* Footer band */
  .web-band {
    position: absolute; left: 0; top: 466px; width: 824px; height: 42px;
    background: var(--green);
    display: flex; align-items: center; justify-content: center; gap: 10px;
    color: var(--band-text); font-size: 22px;
  }
  .web-band svg { width: 22px; height: 22px; }
  .corner-block { position: absolute; left: 929px; top: 466px; width: 63px; height: 41px; background: var(--navy); }
</style>
</head>
<body>
  <main class="card">
    <section class="brand">
      <div class="brand-square"></div>
      <div class="brand-name">Lantern Bridge Advisory, Inc</div>
      <div class="brand-tagline">Clear guidance to buy or sell your local business</div>
    </section>

    <div class="divider"></div>

    <section class="person">
      <h1 class="person-name">Dale R. Whitmore</h1>
      <p class="person-title">Small Business Advisor</p>
    </section>

    <ul class="contacts">
      <li>
        <svg viewBox="0 0 18 18" aria-hidden="true"><rect x="4" y="1" width="10" height="16" rx="1.5" fill="none" stroke="var(--navy)" stroke-width="1.8"/><line x1="7.5" y1="14.5" x2="10.5" y2="14.5" stroke="var(--navy)" stroke-width="1.4"/></svg>
        (917) 555-0148
      </li>
      <li>
        <svg viewBox="0 0 18 18" aria-hidden="true"><path d="M3 2.5l3 -0.5 1.6 3.6-1.8 1.3c.9 2 2.3 3.4 4.3 4.3l1.3-1.8 3.6 1.6-.5 3c-6.8 .3-11.8-4.7-11.5-11.5z" fill="var(--green)"/><path d="M10.5 2.5a5 5 0 0 1 5 5M10.5 5a2.5 2.5 0 0 1 2.5 2.5" fill="none" stroke="var(--green)" stroke-width="1.3"/></svg>
        (718) 555-0193
      </li>
      <li>
        <svg viewBox="0 0 18 18" aria-hidden="true"><rect x="1" y="5" width="16" height="11" fill="var(--green)"/><path d="M1 5l8 6 8-6" fill="none" stroke="#f3efe7" stroke-width="1.3"/><circle cx="9" cy="4.5" r="3" fill="none" stroke="var(--green)" stroke-width="1.3"/></svg>
        d.whitmore@lanternbridgeadvisory.com
      </li>
    </ul>

    <footer class="web-band">
      <svg viewBox="0 0 22 22" aria-hidden="true"><circle cx="11" cy="11" r="9" fill="none" stroke="#eef5e2" stroke-width="1.8"/><ellipse cx="11" cy="11" rx="4" ry="9" fill="none" stroke="#eef5e2" stroke-width="1.4"/><line x1="2" y1="11" x2="20" y2="11" stroke="#eef5e2" stroke-width="1.4"/></svg>
      www.lanternbridgeadvisory.com
    </footer>
    <div class="corner-block"></div>
  </main>
</body>
</html>
```